KALMO-VIT Banner

I need a banner for a outpatient (poli clinic) psychiatric clinic/ mental health care center.
The name of the out-patient clinic is ' KALMO-VIT ' . It is written in capitals. The colour we use is green. Just look at the uploaded files and on our website: WWW.KALMO-VIT.NL

KALMO-VIT is mainly based in the city Groningen, the Netherlands (Holland).

If it is possible, I would also like to have a QR-code of our website on the banner. It should be a vertical banner.

We want to print big vertical flags/ roll-up banners

Reason: I just extended the deadline. I will attach more examples of what I want.

To all designers,

Sorry for not giving feedback on your designs. I have attached a picture that I want to be used as background.

So the colour of the banner should be greenish, with the text: "  KALMO-VIT " 
Further more I would like to have the website on the banner: " WWW.KALMO-VIT.NL "
The logo of KALMO-VIT must also be on the banner
And also a small QR-code

I will extend the deadline till february 13th

thanks,

Joost

Reason: Dear designers, Sorry for not reacting. I was ill and could not work. best regards, Joost

Mental Health

• The logo of KALMO-VIT must be in the design. For the right colour just take a look at the attached files and our website: www.KALMO-VIT.NL

```html
<!DOCTYPE html>
<html lang="en">
<head>
<meta charset="utf-8">
<title>KALMO-VIT Roll-up Banner</title>
<link rel="stylesheet" href="https://fonts.googleapis.com/css2?family=Roboto+Slab:wght@400;700;800&family=Didact+Gothic&family=Carlito&family=Tinos&display=swap">
<style>
  :root {
    --green: #0b8a1c;
    --green-deep: #006410;
    --green-bright: #12a21f;
    --green-edge: #2a9b33;
    --ink: #2b2b2b;
    --white: #ffffff;
    --storm-dark: #1d2a33;
    --storm-mid: #4f6470;
    --storm-light: #9aa9ad;
  }
  * { margin: 0; padding: 0; box-sizing: border-box; }
  html, body {
    width: 711px; height: 1200px; overflow: hidden;
    background: var(--white);
  }
  .canvas { position: relative; width: 711px; height: 1200px; }
  .banner {
    position: absolute; left: 107px; top: 0;
    width: 498px; height: 1200px;
    border-left: 1px solid var(--green-edge);
    border-right: 1px solid var(--green-edge);
    border-top: 1px solid var(--green-edge);
    overflow: hidden;
  }
  .brand {
    position: absolute; top: 26px; left: 0; width: 100%;
    display: flex; justify-content: center; align-items: center; gap: 12px;
  }
  .brand-name {
    font-family: "Tinos", serif;
    font-size: 45px; color: var(--green); letter-spacing: 1px; line-height: 1;
  }
  .brand-mark {
    width: 16px; height: 16px; border-radius: 50%;
    background: var(--green);
  }
  .symptoms {
    position: absolute; top: 107px; left: 0; width: 100%; height: 311px;
    background: linear-gradient(165deg, var(--green-deep) 0%, var(--green) 45%, var(--green-bright) 100%);
    color: var(--white);
    font-family: "Roboto Slab", serif; font-weight: 800;
    font-size: 20px; text-align: center;
  }
  .symptoms p { position: absolute; left: 0; width: 100%; line-height: 1; }
  .symptoms p:nth-child(1) { top: 54px; }
  .symptoms p:nth-child(2) { top: 115px; }
  .symptoms p:nth-child(3) { top: 178px; }
  .symptoms p:nth-child(4) { top: 239px; }
  .hero {
    position: absolute; top: 418px; left: 0; width: 100%; height: 433px;
    background:
      radial-gradient(ellipse at 55% 30%, var(--storm-light) 0%, transparent 45%),
      linear-gradient(180deg, var(--storm-mid) 0%, var(--storm-dark) 55%, #23343c 100%);
  }
  .courage {
    position: absolute; top: 728px; left: 0; width: 100%;
    font-family: "Roboto Slab", serif; font-weight: 400;
    font-size: 27px; line-height: 41px; text-align: center;
    color: var(--white);
  }
  .courage .accent {
    color: var(--green-bright);
    -webkit-text-stroke: 1px #c9f5c9;
  }
  .tagline {
    position: absolute; top: 888px; left: 0; width: 100%;
    text-align: center; font-family: "Didact Gothic", sans-serif;
    font-size: 29px; color: var(--green); line-height: 1;
  }
  .contact {
    position: absolute; top: 966px; left: 0; width: 100%;
    text-align: center; color: var(--ink);
  }
  .contact .call {
    font-family: "Didact Gothic", sans-serif;
    font-size: 29px; line-height: 39px;
  }
  .contact .links {
    margin-top: 8px;
    font-family: "Carlito", sans-serif; font-size: 20px; line-height: 31px;
  }
  .footer-band {
    position: absolute; bottom: 0; left: 0; width: 100%; height: 62px;
    background: var(--green);
  }
</style>
</head>
<body>
<div class="canvas">
  <main class="banner">
    <header class="brand">
      <span class="brand-name">KALMO-VIT</span>
      <span class="brand-mark" aria-hidden="true"></span>
    </header>

    <section class="symptoms">
      <p>Overwhelming feelings of sadness…</p>
      <p>Really “UP” days or “DOWN” days</p>
      <p>that affect your ability</p>
      <p>to function…</p>
    </section>

    <div class="hero" role="img" aria-label="Photo of a man in a suit sitting calmly in an armchair on a stormy sea, holding an umbrella under lightning"></div>

    <p class="courage">
      It takes <span class="accent">COURAGE</span> to ask for<br>
      <span class="accent">HELP</span> with a mental illness,<br>
      <span class="accent">BUT YOU CAN DO IT.</span>
    </p>

    <p class="tagline">STOP MISSING OUT ON LIFE.</p>

    <div class="contact">
      <p class="call">For affordable help,<br>call us we care! - 555-014-072</p>
      <p class="links">Email- info@kalmo-vit.nl<br>www.KALMO-VIT.NL</p>
    </div>

    <div class="footer-band"></div>
  </main>
</div>
</body>
</html>
```